Business Card design for new private practice opening

I need a business card design for my new private practice with my new logo uploaded as a file
On the front the logo
On the back: maybe a small logo somewhere?
Priv. Doz. DDr. Marlene Osterwald
Fachärztin für Allgemein- & Viszeralchirurgie
Address: xxx
Tel: xxx
Mobil:xxx
Webseite:xxx
Email:xxx

Contact Information for Business Card

See project description above for details

Requirements
Nice to have
• I would like the colors of the logo incorporated into the business card

```html
<!DOCTYPE html>
<html lang="de">
<head>
<meta charset="utf-8">
<title>Osterwald Chirurgie – Visitenkarte</title>
<link rel="stylesheet" href="https://fonts.googleapis.com/css2?family=Montserrat:wght@400;500;600&display=swap">
<style>
  :root {
    --teal: #45b5b1;
    --teal-light: #a8d8d6;
    --mist: #e3efef;
    --grey: #7a7a7a;
    --grey-text: #858585;
    --paper: #ffffff;
    --backdrop: #efefef;
  }
  * { margin: 0; padding: 0; box-sizing: border-box; }
  html, body { width: 1200px; height: 1200px; overflow: hidden; }
  body {
    background: var(--backdrop);
    font-family: "Montserrat", sans-serif;
    position: relative;
  }
  .card {
    position: absolute;
    left: 204px;
    width: 794px;
    height: 456px;
    background: var(--paper);
    overflow: hidden;
  }
  .card--front { top: 120px; }
  .card--back { top: 624px; height: 454px; }

  /* Front */
  .brand-mark {
    position: absolute;
    left: 128px; top: 124px;
    width: 156px; height: 156px;
    border-radius: 50%;
    background: var(--teal);
    border: 5px solid var(--grey);
  }
  .brand-name {
    position: absolute;
    left: 312px; top: 132px;
    font-weight: 600;
    font-size: 58px;
    line-height: 68px;
    letter-spacing: 1px;
    color: var(--grey);
    text-transform: uppercase;
  }

  /* Back */
  .person-name {
    position: absolute;
    left: 50px; top: 48px;
    font-weight: 500;
    font-size: 34px;
    color: var(--teal);
    letter-spacing: 0.3px;
  }
  .person-title {
    position: absolute;
    left: 50px; top: 88px;
    font-size: 19px;
    color: var(--grey-text);
    letter-spacing: 0.6px;
    text-transform: uppercase;
  }
  .divider {
    position: absolute;
    left: 50px; top: 120px;
    width: 676px; height: 3px;
    background: linear-gradient(to right, var(--teal) 0%, var(--teal) 40%, rgba(69,181,177,0.15) 100%);
  }
  .contact-list {
    position: absolute;
    left: 50px; top: 134px;
    list-style: none;
  }
  .contact-item {
    display: flex;
    align-items: center;
    height: 47px;
    font-size: 27px;
    color: var(--grey-text);
    letter-spacing: 0.4px;
  }
  .contact-icon {
    width: 22px; height: 22px;
    margin-right: 16px;
    fill: var(--teal);
    flex: none;
  }
  .wave { position: absolute; left: 0; top: 0; }
  .badge {
    position: absolute;
    left: 596px; top: 280px;
    width: 132px; height: 132px;
    border-radius: 50%;
    background: var(--teal);
    border: 4px solid var(--grey);
  }
</style>
</head>
<body>

  <section class="card card--front" aria-label="Vorderseite">
    <div class="brand-mark"></div>
    <div class="brand-name">Osterwald<br>Chirurgie</div>
  </section>

  <section class="card card--back" aria-label="Rückseite">
    <svg class="wave" width="794" height="454" viewBox="0 0 794 454" aria-hidden="true">
      <defs>
        <linearGradient id="mid-fade" x1="0" y1="0" x2="1" y2="0">
          <stop offset="0" stop-color="#ffffff" stop-opacity="0"/>
          <stop offset="0.6" stop-color="#cfe7e6"/>
          <stop offset="1" stop-color="#8fcdca"/>
        </linearGradient>
      </defs>
      <path d="M0 454 C 300 430, 600 360, 794 252 L 794 454 Z" fill="var(--mist)"/>
      <path d="M40 454 C 360 440, 620 400, 794 334 L 794 454 Z" fill="url(#mid-fade)"/>
      <path d="M360 454 C 560 440, 700 420, 794 396 L 794 454 Z" fill="var(--teal)"/>
    </svg>

    <h1 class="person-name">Priv. Doz. DDr. Marlene Osterwald</h1>
    <p class="person-title">Fachärztin für Allgemein- &amp; Viszeralchirurgie</p>
    <div class="divider"></div>

    <ul class="contact-list">
      <li class="contact-item">
        <svg class="contact-icon" viewBox="0 0 24 24"><path d="M12 2a7 7 0 0 0-7 7c0 5 7 13 7 13s7-8 7-13a7 7 0 0 0-7-7zm0 9.5A2.5 2.5 0 1 1 12 6.5a2.5 2.5 0 0 1 0 5z"/></svg>
        Address: xxx
      </li>
      <li class="contact-item">
        <svg class="contact-icon" viewBox="0 0 24 24"><path d="M6.6 10.8a15 15 0 0 0 6.6 6.6l2.2-2.2c.3-.3.7-.4 1-.2 1.1.4 2.3.6 3.6.6.6 0 1 .4 1 1V20c0 .6-.4 1-1 1A17 17 0 0 1 3 4c0-.6.4-1 1-1h3.5c.6 0 1 .4 1 1 0 1.3.2 2.5.6 3.6.1.3 0 .7-.2 1z"/></svg>
        Tel: xxx
      </li>
      <li class="contact-item">
        <svg class="contact-icon" viewBox="0 0 24 24"><path d="M8 2h8a2 2 0 0 1 2 2v16a2 2 0 0 1-2 2H8a2 2 0 0 1-2-2V4a2 2 0 0 1 2-2zm3 16v1h2v-1z"/></svg>
        Mobil: xxx
      </li>
      <li class="contact-item">
        <svg class="contact-icon" viewBox="0 0 24 24"><path d="M12 2a10 10 0 1 0 0 20 10 10 0 0 0 0-20zm6.9 6h-3a15 15 0 0 0-1.3-3.9A8 8 0 0 1 18.9 8zM12 4c.8 1.2 1.5 2.5 1.9 4h-3.8c.4-1.5 1.1-2.8 1.9-4zM4.3 14a8 8 0 0 1 0-4h3.4a16 16 0 0 0 0 4zm.8 2h3a15 15 0 0 0 1.3 3.9A8 8 0 0 1 5.1 16zm3-8h-3a8 8 0 0 1 4.3-3.9A15 15 0 0 0 8.1 8zM12 20c-.8-1.2-1.5-2.5-1.9-4h3.8c-.4 1.5-1.1 2.8-1.9 4zm2.3-6H9.7a14 14 0 0 1 0-4h4.6a14 14 0 0 1 0 4zm.3 5.9a15 15 0 0 0 1.3-3.9h3a8 8 0 0 1-4.3 3.9zm1.7-5.9a16 16 0 0 0 0-4h3.4a8 8 0 0 1 0 4z"/></svg>
        Webseite: xxx
      </li>
      <li class="contact-item">
        <svg class="contact-icon" viewBox="0 0 24 24"><path d="M3 5h18a1 1 0 0 1 1 1v.5l-10 6-10-6V6a1 1 0 0 1 1-1zm-1 3.8 10 6 10-6V18a1 1 0 0 1-1 1H3a1 1 0 0 1-1-1z"/></svg>
        Email: xxx
      </li>
    </ul>

    <div class="badge"></div>
  </section>

</body>
</html>
```